Design business cards for Ironvale Barbers (Opening March so won't need finalised till January2018

Ironvale Barbers is the new age barbers and skincare for all men. Creating tailor made haircuts & customised skincare solutions for the perfect healthy manly look. The Barbers will have a industrial, rustic, worldly feel about it. Rustic red brick wall with old wine barrels as the work stations with the old fashion barber chairs. Concrete floor and a bit corrugated iron around.
Target Market(s)
Professional males who like a great haircut, wet shave and may consider a facial if in the right environment. Total pampering experience in a boys environment.
Industry/Entity Type
Barber
Contact Information for Business Card
Front- Logo - address is 42 Kowhai Rd Taupo
Ph - (07) 548 9163
www.ironvalebarbers.com
email - hello@ironvale.co.nz
Back of card
Mens Haircare - Wet Shaving - Facials - Skin Prescriptions
We are doing a loyalty program - 6 squares numbered then 7th free
Colors
Designer to choose colors to be used in the design.
Requirements
Must have
- Clean simple easy to read.
Nice to have
- Our current colours are white font on black background but thinking we need to introduce another colour. Maybe white logo on a copper, bronze or rusty background. Or even a rustic red brick wall with white writing. Want it clean simple to read. Maybe a burgundy?
Should not have
- no images like heads, scissors, razors please

```html
<!DOCTYPE html>
<html lang="en">
<head>
<meta charset="utf-8">
<title>Ironvale Barbers – Business Cards</title>
<link href="https://fonts.googleapis.com/css2?family=Raleway:wght@400;600&display=swap" rel="stylesheet">
<style>
  :root {
    --backdrop: #262727;
    --card: #3b3c3c;
    --card-edge: #333434;
    --ink: #f1f1ef;
    --ink-soft: #d4d4d1;
    --frame: #c9c9c6;
  }
  * { margin: 0; padding: 0; box-sizing: border-box; }
  html, body {
    width: 1200px; height: 900px; overflow: hidden;
    background: var(--backdrop);
    font-family: "Raleway", Arial, sans-serif;
    color: var(--ink);
  }
  .canvas { position: relative; width: 1200px; height: 900px; }

  .card {
    position: absolute;
    width: 540px; height: 309px;
    background: radial-gradient(ellipse at 45% 40%, #424343 0%, var(--card) 55%, var(--card-edge) 100%);
    box-shadow: 0 18px 40px rgba(0,0,0,.55);
  }
  .card--services { left: 70px; top: 110px; }
  .card--contact  { left: 590px; top: 480px; }

  .card__frame {
    position: absolute; inset: 16px;
    border: 1.5px solid var(--frame);
  }
  .card__frame::after {
    content: ""; position: absolute; inset: 5px;
    border: 1px solid var(--frame); opacity: .55;
  }
  .card__corner {
    position: absolute; width: 10px; height: 10px;
    background: var(--card); border: 1.5px solid var(--frame);
  }
  .card__corner--tl { left: 11px; top: 11px; }
  .card__corner--tr { right: 11px; top: 11px; }
  .card__corner--bl { left: 11px; bottom: 11px; }
  .card__corner--br { right: 11px; bottom: 11px; }

  .wordmark {
    position: absolute; left: 0; right: 0; top: 62px;
    text-align: center; font-weight: 600; color: var(--ink);
    line-height: 1;
  }
  .wordmark__name { display: block; font-size: 50px; letter-spacing: 2px; text-transform: uppercase; }
  .wordmark__trade { display: block; margin-top: 8px; font-size: 18px; letter-spacing: 7px; text-transform: uppercase; }

  .services {
    position: absolute; left: 0; right: 0; top: 185px;
    text-align: center; font-size: 14px; color: var(--ink-soft);
    letter-spacing: .3px;
  }
  .services span.sep { margin: 0 10px; }

  .appointment {
    position: absolute; left: 0; right: 0; top: 226px;
    display: flex; justify-content: center; gap: 18px;
    font-size: 14px; color: var(--ink-soft);
  }
  .appointment__field { display: flex; align-items: flex-end; gap: 6px; }
  .appointment__line { display: inline-block; width: 130px; border-bottom: 1px solid var(--ink-soft); margin-bottom: 4px; }

  .contact {
    position: absolute; left: 0; right: 0; top: 184px;
    display: grid; grid-template-columns: auto auto;
    justify-content: center; column-gap: 30px; row-gap: 16px;
    font-size: 14.5px; color: var(--ink-soft);
  }
  .contact__item { display: flex; align-items: center; gap: 7px; }
  .contact__item svg { width: 14px; height: 14px; fill: var(--ink-soft); flex: none; }
</style>
</head>
<body>
<main class="canvas">

  <section class="card card--services" aria-label="Services card">
    <div class="card__frame"></div>
    <span class="card__corner card__corner--tl"></span>
    <span class="card__corner card__corner--tr"></span>
    <span class="card__corner card__corner--bl"></span>
    <span class="card__corner card__corner--br"></span>

    <h2 class="wordmark">
      <span class="wordmark__name">Ironvale</span>
      <span class="wordmark__trade">Barbers</span>
    </h2>

    <p class="services">
      Mens Haircare<span class="sep">|</span>Wet Shaving<span class="sep">|</span>Facials<span class="sep">|</span>Skin Prescriptions
    </p>

    <div class="appointment">
      <span class="appointment__field">Date - <span class="appointment__line"></span></span>
      <span class="appointment__field">Time - <span class="appointment__line"></span></span>
    </div>
  </section>

  <section class="card card--contact" aria-label="Contact card">
    <div class="card__frame"></div>
    <span class="card__corner card__corner--tl"></span>
    <span class="card__corner card__corner--tr"></span>
    <span class="card__corner card__corner--bl"></span>
    <span class="card__corner card__corner--br"></span>

    <h1 class="wordmark">
      <span class="wordmark__name">Ironvale</span>
      <span class="wordmark__trade">Barbers</span>
    </h1>

    <div class="contact">
      <span class="contact__item">
        <svg viewBox="0 0 16 16" aria-hidden="true"><path d="M8 0a5.5 5.5 0 0 0-5.5 5.5C2.5 10 8 16 8 16s5.5-6 5.5-10.5A5.5 5.5 0 0 0 8 0zm0 8a2.5 2.5 0 1 1 0-5 2.5 2.5 0 0 1 0 5z"/></svg>
        42 Kowhai Rd Taupo
      </span>
      <span class="contact__item">
        <svg viewBox="0 0 16 16" aria-hidden="true"><path d="M0 3h16v1.2L8 9 0 4.2z"/><path d="M0 5.6l8 4.8 8-4.8V13H0z"/></svg>
        hello@ironvale.co.nz
      </span>
      <span class="contact__item">
        <svg viewBox="0 0 16 16" aria-hidden="true"><path d="M1 5c0-1.5 3-3 7-3s7 1.5 7 3v1.5h-3.5V5h-7v1.5H1z"/><path d="M3 8h10l1 6H2z"/></svg>
        000 000 0000
      </span>
      <span class="contact__item">www.ironvalebarbers.com</span>
    </div>
  </section>

</main>
</body>
</html>
```